Discreet simple classy for adult entertainment

I would like a matte black business card with gold writing for my business. Keeping it simple. Having my following:

Lana frost
Events. Entertainment. Promotions
0491726580

or alternatively could have what i had on my previous card below but i think i prefer the above as again - discretion.

Maybe a nice gold line thru the card or some other very simple design . Or not open to ideas/ can be doublesided if any good ideas with that.

included pics of my old bus card. not sure weather i want a photo on it or not. if i do it wont be the same pic. i kinda wanted a card that was discreet so if it was in someones wallet they wouldn't neccessarily realise it was from a stripper.

Target Market(s)

men

Industry/Entity Type

Business

Contact Information for Business Card

Lana frost
0491726580

Requirements
Nice to have
• i don't know i am really open to anything. im giving my cards to guys so something they can have in their wallet that is discreet preferably.

```html
<!DOCTYPE html>
<html lang="en">
<head>
<meta charset="utf-8">
<title>Lana Frost – Business Card</title>
<link rel="stylesheet" href="https://fonts.googleapis.com/css2?family=Josefin+Sans:wght@300;400&display=swap">
<style>
  :root {
    --backdrop: #e9e6e1;
    --card-dark: #141414;
    --card-mid: #1e1e1e;
    --card-light: #2c2c2c;
    --gold: #c9a75a;
    --gold-soft: #b8975022;
    --gold-light: #e3c886;
    --gold-deep: #9c7c3a;
    --band-ink: #1a1a1a;
  }
  * { margin: 0; padding: 0; box-sizing: border-box; }
  html, body {
    width: 1200px; height: 1022px; overflow: hidden;
    background: var(--backdrop);
    font-family: "Josefin Sans", Arial, sans-serif;
  }
  .card {
    position: absolute; left: 90px; top: 226px;
    width: 1020px; height: 570px;
    border-radius: 18px; overflow: hidden;
    background: radial-gradient(ellipse at 40% 40%, var(--card-light), var(--card-mid) 50%, var(--card-dark));
    box-shadow: 0 18px 40px rgba(0,0,0,.35);
  }
  .portrait-area {
    position: absolute; left: 60px; top: 40px; width: 520px; height: 480px;
    background: radial-gradient(ellipse at 45% 50%, rgba(90,90,90,.35), rgba(50,50,50,.12) 60%, transparent 75%);
  }
  .band {
    position: absolute; right: 0; top: 0; width: 220px; height: 100%;
  }
  .name {
    position: absolute; left: 70px; top: 90px;
    color: var(--gold);
    font-weight: 300; font-size: 64px; letter-spacing: 10px;
    text-transform: uppercase; white-space: nowrap;
  }
  .divider {
    position: absolute; left: 70px; top: 330px; width: 720px; height: 1.5px;
    background: var(--gold);
  }
  .services {
    position: absolute; left: 78px; top: 350px;
    list-style: none; color: var(--gold);
    font-size: 25px; line-height: 34px; font-weight: 300;
  }
  .services li::before { content: "\2022"; margin-right: 12px; }
  .contact {
    position: absolute; right: 240px; top: 240px; text-align: right;
    color: var(--gold); font-size: 22px; line-height: 34px; font-weight: 300;
    white-space: nowrap;
  }
  .handle {
    position: absolute; right: 30px; top: 40px;
    color: var(--band-ink); font-size: 22px; font-weight: 400;
  }
</style>
</head>
<body>
  <div class="card">
    <div class="portrait-area" role="img" aria-label="Faint black and white portrait photograph of a woman"></div>
    <svg class="band" viewBox="0 0 220 570" preserveAspectRatio="none" aria-hidden="true">
      <defs>
        <linearGradient id="band-gold" x1="0" y1="0" x2="1" y2="1">
          <stop offset="0" stop-color="#e3c886"/>
          <stop offset="1" stop-color="#c9a75a"/>
        </linearGradient>
      </defs>
      <polygon points="70,0 220,0 220,570 150,570 150,330 70,250" fill="url(#band-gold)"/>
      <polygon points="150,330 150,570 158,570 158,336" fill="#9c7c3a"/>
    </svg>
    <div class="handle">lanafrost</div>
    <h1 class="name">Lana Frost</h1>
    <div class="contact">
      <p>P. 0491 726 580</p>
      <p>Events-Entertainment-Promotions</p>
    </div>
    <div class="divider"></div>
    <ul class="services">
      <li>Bikini Barmaid</li>
      <li>Poker Dealer</li>
      <li>Professional Party Waitress</li>
    </ul>
  </div>
</body>
</html>
```